Bref créative
Brightpath Outcomes Inc
I need double sided standard sized Business Card [3.5" x 2"]
You decid
Professional
Danielle Hartwell
CEO
4172 Juniper Ridge Drive,
Suite 517
West Bloomfield, MI 48109
danielle.hartwell@brightpathoutcomes.example
www.brightpathoutcomes.example
On the back of the card we want another web adrdress of
walkingherownroute.example

```html
<!DOCTYPE html>
<html lang="en">
<head>
<meta charset="utf-8">
<title>Brightpath Outcomes Inc — Stationery</title>
<link href="https://fonts.googleapis.com/css2?family=Open+Sans:wght@400;600;700&display=swap" rel="stylesheet">
<style>
:root{
  --bg:#e9e7e4;
  --paper:#ffffff;
  --red:#e2372b;
  --red-dark:#b8241b;
  --charcoal:#2b2b2d;
  --graphite:#4a4a4c;
  --ink:#333333;
  --muted:#8a8a8a;
  --faint:#f1f1f1;
}
*{box-sizing:border-box;margin:0;padding:0}
html,body{width:1200px;height:410px;overflow:hidden}
body{background:var(--bg);font-family:"Open Sans",Arial,sans-serif;color:var(--ink);position:relative}
.piece{position:absolute;box-shadow:0 2px 6px rgba(0,0,0,.25);overflow:hidden}
.card{width:180px;height:96px}
.card-front{background:var(--paper)}
.card-dark{background:var(--charcoal);color:#fff}
.card-back-red{background:linear-gradient(135deg,var(--red) 0%,var(--red-dark) 100%)}
.card-back-grey{background:linear-gradient(135deg,var(--graphite) 0%,#2f2f31 100%)}
.brand{display:flex;align-items:center;gap:4px;font-weight:700;text-transform:uppercase;letter-spacing:.3px;line-height:1.05}
.brand-mark{width:7px;height:7px;flex:none}
.brand-block{position:absolute;left:10px;top:8px;background:var(--red);color:#fff;padding:5px 6px;font-size:6px;width:62px;z-index:1}
.brand-block .brand-mark{background:#fff}
.holder{position:absolute;left:82px;top:12px;white-space:nowrap}
.holder-name{font-size:8px;font-weight:700}
.holder-title{font-size:6px;color:var(--muted)}
.contact{position:absolute;left:10px;top:50px;font-size:4.6px;line-height:1.55;white-space:nowrap}
.card-dark .contact{color:#ddd}
.card-dark .holder-title{color:#bbb}
.dark-rule{position:absolute;left:0;top:42px;width:100%;height:2px;background:var(--red)}
.back-url{position:absolute;left:0;right:0;top:44px;text-align:center;font-size:5px;color:#fff;letter-spacing:.6px}
.silhouette-area{position:absolute;background:radial-gradient(ellipse at 60% 50%,#ececec 0%,#f6f6f6 55%,rgba(255,255,255,0) 75%)}
.envelope{background:var(--paper)}
.env-front{left:67px;top:247px;width:264px;height:118px}
.env-front .brand-block{left:10px;top:10px;width:80px;font-size:6.5px}
.env-front .silhouette-area{left:190px;top:4px;width:70px;height:110px}
.env-address{position:absolute;left:10px;bottom:8px;font-size:4.5px;color:var(--muted);white-space:nowrap}
.env-back{left:348px;top:247px;width:252px;height:118px}
.env-flap{position:absolute;left:0;top:0}
.env-flap-brand{position:absolute;left:0;right:0;top:18px;justify-content:center;color:#fff;font-size:6px}
.env-flap-brand .brand-mark{background:var(--red)}
.letterhead{width:228px;height:360px;top:30px;background:var(--paper)}
.lh-1{left:629px}
.lh-2{left:893px}
.letterhead .brand-block{left:20px;top:14px;width:90px;font-size:7px;padding:6px 7px}
.letterhead .silhouette-area{left:110px;top:40px;width:118px;height:270px}
.lh-footer{position:absolute;left:20px;right:20px;bottom:14px;font-size:4.5px;color:var(--muted);line-height:1.6;white-space:nowrap}
.lh-footer .accent{color:var(--red)}
</style>
</head>
<body>

<div class="piece card card-front" style="left:60px;top:40px">
  <div class="brand brand-block"><span class="brand-mark"></span>Brightpath Outcomes</div>
  <div class="holder"><div class="holder-name">Danielle Hartwell</div><div class="holder-title">CEO</div></div>
  <div class="contact">4172 Juniper Ridge Drive, Suite 517<br>West Bloomfield, MI 48109<br>danielle.hartwell@brightpathoutcomes.example<br>www.brightpathoutcomes.example</div>
</div>
<div class="piece card card-front" style="left:60px;top:142px">
  <div class="brand brand-block"><span class="brand-mark"></span>Brightpath Outcomes</div>
  <div class="holder"><div class="holder-name">Danielle Hartwell</div><div class="holder-title">CEO</div></div>
  <div class="contact">4172 Juniper Ridge Drive, Suite 517<br>West Bloomfield, MI 48109<br>danielle.hartwell@brightpathoutcomes.example<br>www.brightpathoutcomes.example</div>
</div>

<div class="piece card card-dark" style="left:246px;top:40px">
  <div class="brand brand-block"><span class="brand-mark"></span>Brightpath Outcomes</div>
  <div class="holder"><div class="holder-name">Danielle Hartwell</div><div class="holder-title">CEO</div></div>
  <div class="dark-rule"></div>
  <div class="contact">4172 Juniper Ridge Drive, Suite 517<br>West Bloomfield, MI 48109<br>danielle.hartwell@brightpathoutcomes.example<br>www.brightpathoutcomes.example</div>
</div>
<div class="piece card card-dark" style="left:246px;top:142px">
  <div class="brand brand-block"><span class="brand-mark"></span>Brightpath Outcomes</div>
  <div class="holder"><div class="holder-name">Danielle Hartwell</div><div class="holder-title">CEO</div></div>
  <div class="dark-rule"></div>
  <div class="contact">4172 Juniper Ridge Drive, Suite 517<br>West Bloomfield, MI 48109<br>danielle.hartwell@brightpathoutcomes.example<br>www.brightpathoutcomes.example</div>
</div>

<div class="piece card card-back-red" style="left:432px;top:40px">
  <div class="back-url">www.walkingherownroute.example</div>
</div>
<div class="piece card card-back-grey" style="left:432px;top:142px">
  <div class="back-url">www.walkingherownroute.example</div>
</div>

<div class="piece envelope env-front">
  <div class="silhouette-area" role="img" aria-label="Faint profile silhouette decoration"></div>
  <div class="brand brand-block"><span class="brand-mark"></span>Brightpath Outcomes</div>
  <div class="env-address">4172 Juniper Ridge Drive, Suite 517 · West Bloomfield, MI 48109</div>
</div>

<div class="piece envelope env-back">
  <svg class="env-flap" width="252" height="70" viewBox="0 0 252 70" aria-hidden="true">
    <path d="M0 0 H252 L138 66 Q126 72 114 66 Z" fill="#3a3a3c"/>
  </svg>
  <div class="brand env-flap-brand"><span class="brand-mark"></span>Brightpath Outcomes</div>
</div>

<div class="piece letterhead lh-1">
  <div class="silhouette-area" role="img" aria-label="Faint profile silhouette decoration"></div>
  <div class="brand brand-block"><span class="brand-mark"></span>Brightpath Outcomes</div>
  <div class="lh-footer"><span class="accent">■</span> 4172 Juniper Ridge Drive, Suite 517, West Bloomfield, MI 48109<br><span class="accent">■</span> www.brightpathoutcomes.example</div>
</div>
<div class="piece letterhead lh-2">
  <div class="silhouette-area" role="img" aria-label="Faint profile silhouette decoration"></div>
  <div class="brand brand-block"><span class="brand-mark"></span>Brightpath Outcomes</div>
  <div class="lh-footer"><span class="accent">■</span> 4172 Juniper Ridge Drive, Suite 517, West Bloomfield, MI 48109<br><span class="accent">■</span> www.brightpathoutcomes.example</div>
</div>

</body>
</html>
```